Beauty care products face masks Layout

--- English below --- We need a label set (2 pieces á 35x80mm) for a black 50ml tube. The logo and the subtitles are displayed in the Annexes. A black drop should be incorporated into the label. Brand Name: lumaV Product name: sable subtitles: Deep cleansing peel-off mask required entry is: 50 ml / 1.69 fl.oz. On the back: Recommended use: In order to achieve the best results for you, we recommend that you clean your face thoroughly and dry. Apply the mask, thereby avoiding the mouth and eye area. After 20-30 minutes the mask is dried and can be pulled off. Purify by removing the mask, your face with warm water. We recommend a calming face cream after the application to use. The mask Please do not dispose of in the toilet. Application: Every 2-3 days Ingredients (ingredients): Water, Polyvinyl Alcohol, Glycerin, Citrus Paradisi, PEG-8, panthenol, Fragrance, Cellulose Gum, tetra sodium EDTA, Activated carbon, Rosemary Extract, Avena sativa Extract, Pot Marigold , Zinc Gluconate, lecithin, Retinyl Palmitate, arachidyl propionate, tocopheryl acetate, ethyl Liloenate, xanthan Gum, Limonene, linalool, geraniol, methyl paraben English: We need a label set (2 pieces 35mm wide 80mm height) for a black 50ml tube. You can find the logo as well as the subtitel in the attachments. Brand Name: lumaV Product Name: sable Subtitle: Deep cleansing peel-off mask On the back label: Recommended use: In order to achieve the best results for you, we recommend that you clean your face thoroughly and dry. Apply the mask, thereby avoiding the mouth and eye area. After 20-30 minutes the mask is dried and can be pulled off. Purify by removing the mask, your face with warm water. We recommend a calming face cream after the application to use. The mask Please do not dispose of in the toilet. Application: Every 2-3 days Ingredients (ingredients): Water, Polyvinyl Alcohol, Glycerin, Citrus Paradisi, PEG-8, panthenol, Fragrance, Cellulose Gum, tetra sodium EDTA, Activated carbon, Rosemary Extract, Avena sativa Extract, Pot Marigold , Zinc Gluconate, lecithin, Retinyl Palmitate, arachidyl propionate, tocopheryl acetate, ethyl Liloenate, xanthan Gum, Limonene, linalool, geraniol, methyl paraben

Target Market(s)

Cosmetics, Beauty, Body Care, Women

Requirements
Must have
• Clear lines to possibly expanding the range Clear design for possible other products
Nice to have
• The design should be more female. We prefer a feminine design.

```html
<!DOCTYPE html>
<html lang="en">
<head>
<meta charset="utf-8">
<title>lumaV – Deep cleansing peel-off mask label set</title>
<link rel="stylesheet" href="https://fonts.googleapis.com/css2?family=Exo+2:wght@400&display=swap">
<style>
  :root {
    --backdrop: #bcbcbc;
    --label-black: #050505;
    --panel-grey: #262626;
    --ink-light: #e6e6e6;
    --ink-soft: #b5b5b5;
    --band-light: #e9e9e9;
    --band-shade: #bdbdbd;
    --ink-dark: #2b2b2b;
  }
  * { margin: 0; padding: 0; box-sizing: border-box; }
  html, body {
    width: 1200px; height: 844px; overflow: hidden;
    background: var(--backdrop);
    font-family: "Exo 2", sans-serif;
  }
  .label-set {
    position: absolute; left: 0; top: 0; width: 1200px; height: 844px;
  }
  .label {
    position: absolute; top: 69px; height: 512px; overflow: hidden;
  }
  /* front label */
  .label--front {
    left: 87px; width: 226px; background: var(--label-black);
  }
  .front__texture {
    position: absolute; left: 0; top: 110px; width: 226px; height: 340px;
    background: radial-gradient(ellipse 90% 60% at 55% 70%, rgba(150,150,150,0.35), rgba(60,60,60,0.15) 55%, transparent 80%);
  }
  .brand-name {
    position: absolute; left: 22px; top: 48px;
    font-weight: 400; font-size: 28px; line-height: 1;
    color: var(--ink-light);
  }
  .product-subtitle {
    position: absolute; right: 23px; top: 331px; width: 150px;
    text-align: right; font-size: 10px; line-height: 14px; font-weight: 400;
    color: var(--ink-light);
  }
  .maker-band {
    position: absolute; left: 0; top: 386px; width: 226px; height: 35px;
    background: linear-gradient(90deg, var(--band-light), #f7f7f7 50%, var(--band-shade));
    font-size: 11px; line-height: 35px; padding-left: 13px; color: var(--ink-dark);
  }
  .volume {
    position: absolute; right: 10px; top: 461px;
    font-size: 11px; color: var(--ink-light);
  }
  /* back label */
  .label--back {
    left: 334px; width: 224px; background: var(--label-black);
  }
  .back__usage-panel {
    position: absolute; left: 0; top: 0; width: 106px; height: 512px;
    background: var(--panel-grey);
  }
  .back__copy {
    position: absolute; top: 78px; height: 416px;
    writing-mode: vertical-rl; transform: rotate(180deg);
    font-size: 6.4px; line-height: 9px; color: var(--ink-soft);
  }
  .back__copy--usage { left: 32px; width: 64px; }
  .back__copy--ingredients { left: 120px; width: 66px; }
</style>
</head>
<body>
<main class="label-set">
  <section class="label label--front">
    <div class="front__texture" role="img" aria-label="Fine dotted wave pattern fading across the label"></div>
    <div class="brand-name">lumaV</div>
    <p class="product-subtitle">Deep cleansing<br>peel-off mask</p>
    <div class="maker-band">by Vellora | Aldenburg</div>
    <div class="volume">50 ml / 1.69 fl.oz.</div>
  </section>

  <section class="label label--back">
    <div class="back__usage-panel"></div>
    <p class="back__copy back__copy--usage">Application:<br>To achieve the best results for you, please clean your face and dry thoroughly. Then apply the mask, avoiding the mouth and eye area. After 20-30 minutes the mask is dried and can be pulled off. After removing the mask, rinse face with warm water. The mask: Please do not dispose of in the toilet.</p>
    <p class="back__copy back__copy--ingredients">Ingredients (Ingrediënts):<br>Water, Polyvinyl Alcohol, Glycerin, Citrus Paradisi, PEG-8, panthenol, Fragrance, Cellulose Gum, tetra sodium EDTA, Activated carbon, Rosemary Extract, Avena sativa Extract, Pot Marigold, Zinc Gluconate, Lecithin, Retinyl Palmitate, arachidyl propionate, tocopheryl acetate, ethyl Linoleate, xanthan Gum, Limonene, linalool, geraniol, methyl paraben</p>
  </section>
</main>
</body>
</html>
```